Falcon ridge RV Retreat business card

I need a design card for the logo I just had made on here. I will provide it and please make some cool designs, thank you.

I would like the card to have
- phone number (865-219-7652)
- email ( falconridgerv@examplemail.com)
- address to the park ( 5186 Copper Kettle Hollow rd, Alder Springs, CR) ZIP: 37946
on the back for double sided id like some lines for writing on. thanks

please follow the logo we provided in the files, I can provide the photoshop file if you need it.

please note this is in the Smokey mountains of Tennessee

Target Market(s)

cabin/rv rentals

Industry/Entity Type

rv/campground/cabin rentals

Contact Information for Business Card

address/email/phone number I added details in brief

Requirements
Must have
• on the back add a bear or something cool

```html
<!DOCTYPE html>
<html lang="en">
<head>
<meta charset="utf-8">
<title>Falcon ridge RV Retreat — Business Card</title>
<link href="https://fonts.googleapis.com/css2?family=Cinzel:wght@500&family=Roboto:wght@400;500&display=swap" rel="stylesheet">
<style>
  :root {
    --page: #d6d7d9;
    --paper: #ffffff;
    --sky: #7fb6dc;
    --sky-deep: #5f9fce;
    --charcoal: #262a2b;
    --accent: #f2ea2c;
    --ink: #1f2224;
    --rule: #3a3a3a;
    --light: #f4f4f4;
  }
  * { box-sizing: border-box; margin: 0; padding: 0; }
  html, body { width: 1200px; height: 900px; overflow: hidden; }
  body {
    background: var(--page);
    display: flex;
    flex-direction: column;
    align-items: center;
    justify-content: center;
    gap: 60px;
    font-family: "Roboto", sans-serif;
  }
  .card {
    position: relative;
    width: 560px;
    height: 320px;
    overflow: hidden;
    box-shadow: 0 6px 18px rgba(0,0,0,0.18);
  }

  .brand-name {
    font-family: "Roboto", sans-serif;
    font-weight: 500;
    color: var(--ink);
    line-height: 1.3;
  }

  /* Back side */
  .card-back { background: var(--paper); }
  .back-brand {
    position: absolute;
    left: 36px; top: 0; bottom: 0;
    width: 190px;
    display: flex; align-items: center; justify-content: center;
  }
  .back-brand .brand-name { font-size: 20px; text-align: center; }
  .writing-lines {
    position: absolute;
    left: 260px; right: 36px; top: 48px;
    display: flex; flex-direction: column; gap: 38px;
  }
  .writing-lines span { display: block; height: 1px; background: var(--rule); }

  /* Front side */
  .card-front { background: linear-gradient(160deg, var(--sky) 0%, var(--sky-deep) 100%); }
  .front-shapes { position: absolute; inset: 0; }
  .front-brand {
    position: absolute; right: 24px; top: 30px; width: 140px;
  }
  .front-brand .brand-name { font-size: 14px; text-align: right; }
  .person {
    position: absolute; left: 30px; top: 118px;
  }
  .person-name {
    font-family: "Cinzel", serif; font-weight: 500;
    color: var(--accent); font-size: 34px; letter-spacing: 1px;
  }
  .person-role {
    color: var(--ink); font-size: 13px; letter-spacing: 2px; margin-top: 2px;
  }
  .contacts {
    position: absolute; left: 205px; top: 232px;
    list-style: none; color: var(--light); font-size: 13px;
    display: flex; flex-direction: column; gap: 6px;
  }
  .contacts li { display: flex; align-items: center; gap: 8px; }
  .contacts svg { width: 13px; height: 13px; flex: none; }
  .address {
    position: absolute; right: 24px; top: 140px;
    color: var(--light); font-size: 13px; line-height: 1.5; text-align: right;
    font-style: normal;
  }
</style>
</head>
<body>

  <section class="card card-back" aria-label="Card back">
    <div class="back-brand">
      <p class="brand-name">Falcon ridge<br>RV Retreat</p>
    </div>
    <div class="writing-lines" aria-hidden="true">
      <span></span><span></span><span></span><span></span><span></span><span></span>
    </div>
  </section>

  <section class="card card-front" aria-label="Card front">
    <svg class="front-shapes" viewBox="0 0 560 320" aria-hidden="true">
      <polygon points="150,320 190,215 310,215 340,110 560,110 560,320" fill="var(--charcoal)"/>
      <polyline points="150,320 190,214 310,214" fill="none" stroke="var(--accent)" stroke-width="4"/>
    </svg>

    <div class="front-brand">
      <p class="brand-name">Falcon ridge<br>RV Retreat</p>
    </div>

    <div class="person">
      <h1 class="person-name">Warren Hale</h1>
      <p class="person-role">DIRECTOR</p>
    </div>

    <ul class="contacts">
      <li>
        <svg viewBox="0 0 16 16"><path fill="var(--accent)" d="M3 1h3l1.5 4-2 1.2a9 9 0 0 0 4.3 4.3L11 8.5l4 1.5v3c0 1-1 2-2 2A13 13 0 0 1 1 3c0-1 1-2 2-2z"/></svg>
        (865-219-7652)
      </li>
      <li>
        <svg viewBox="0 0 16 16"><rect x="1" y="3" width="14" height="10" fill="var(--accent)"/><path d="M1 3l7 6 7-6" fill="none" stroke="var(--charcoal)" stroke-width="1.4"/></svg>
        falconridgerv@examplemail.com
      </li>
      <li>
        <svg viewBox="0 0 16 16"><circle cx="8" cy="8" r="6.5" fill="none" stroke="var(--accent)" stroke-width="1.5"/><path d="M1.5 8h13M8 1.5c-3 3.5-3 9.5 0 13M8 1.5c3 3.5 3 9.5 0 13" fill="none" stroke="var(--accent)" stroke-width="1.2"/></svg>
        www.falconridgerv.example
      </li>
    </ul>

    <address class="address">5186 Copper Kettle Hollow rd,<br>Alder Springs, CR, ZIP: 37946</address>
  </section>

</body>
</html>
```